Brava-Lux.ch is looking for business card letterhead and envelope C5 with WOW effect

We need a strong business card for our company Brava-Lux.ch, logo is available. You want a black or dark background on which the logo Stark r% 26 # 252; appears. Letterhead and envelope in C5 format should be in a similar design, but does not have to be We need a strong business card for our company Brava-Lux.ch, logo is available. A black or dark background is desired, on which the logo Stark comes across. The letterhead and the envelope in C5 format should have a similar design.

Target Market(s)

Private customers as well as entrepreneurs

Contact Information for Business Card

E-mail: info@brava-lux.ch
Web.www.Brava-Lux.ch
Tel: +41 ( 0 ) 79 384 6027
Adresse:
Kellerweg 14
9405 Ostheim

Hier kann man Icons verwenden für Email,Tel und Adressse

Font styles to use
Other font styles liked:
• Dubai,bold

Colors

Designer to choose colors to be used in the design.

Requirements
Must have
• WOW effect
Nice to have
• R% 26 # 252; back business card with our service listings. - VEHICLE LABELING - SHOP WINDOW LABELING - STICKERS AND MUCH MORE ... in red color

```html
<!DOCTYPE html>
<html lang="de">
<head>
<meta charset="utf-8">
<title>Brava-Lux.ch – Visitenkarte</title>
<link rel="stylesheet" href="https://fonts.googleapis.com/css2?family=Open+Sans:wght@600;700&display=swap">
<style>
  :root {
    --stage: #8e8e8e;
    --card-base: #1b2138;
    --card-glow: #2f55b8;
    --card-glow-soft: #203a86;
    --accent: #fcc31c;
    --ink-light: #ffffff;
    --ink-dark: #1d2236;
  }
  * { margin: 0; padding: 0; box-sizing: border-box; }
  html, body { width: 1200px; height: 1200px; overflow: hidden; }
  body {
    background: var(--stage);
    font-family: "Open Sans", Arial, sans-serif;
    position: relative;
  }
  .card {
    position: absolute;
    left: 250px;
    width: 700px;
    height: 400px;
    border-radius: 18px;
    overflow: hidden;
    background: var(--card-base);
  }
  .card--front { top: 190px; }
  .card--back { top: 610px; }
  .card__backdrop {
    position: absolute; inset: 0;
    background:
      radial-gradient(circle at 45% 50%, rgba(47,85,184,.75), transparent 38%),
      radial-gradient(circle at 80% 30%, rgba(32,58,134,.7), transparent 40%),
      radial-gradient(circle at 20% 20%, rgba(32,58,134,.55), transparent 35%),
      linear-gradient(160deg, #1e2748 0%, #18203a 60%, #161c30 100%);
  }
  .brand { position: absolute; display: flex; align-items: center; }
  .brand__dot {
    border-radius: 50%;
    background: var(--accent);
  }
  .brand__name {
    color: var(--ink-light);
    font-weight: 700;
    letter-spacing: 1px;
    text-transform: uppercase;
    white-space: nowrap;
  }
  .card--front .brand { left: 110px; top: 120px; gap: 40px; }
  .card--front .brand__dot { width: 150px; height: 150px; }
  .card--front .brand__name { font-size: 44px; }
  .card--back .brand { left: 190px; top: 52px; gap: 40px; }
  .card--back .brand__dot { width: 110px; height: 110px; }
  .card--back .brand__name { font-size: 29px; }

  .contact {
    position: absolute;
    height: 31px;
    background: var(--accent);
    clip-path: polygon(12px 0, calc(100% - 12px) 0, 100% 50%, calc(100% - 12px) 100%, 12px 100%, 0 50%);
    display: flex; align-items: center;
    padding-left: 26px;
    gap: 10px;
    color: var(--ink-dark);
    font-weight: 600;
    font-size: 18px;
    white-space: nowrap;
  }
  .contact--left { left: 83px; width: 268px; }
  .contact--right { left: 348px; width: 268px; }
  .contact--noicon { padding-left: 58px; }
  .contact__icon { width: 22px; height: 22px; flex: none; }
</style>
</head>
<body>

<section class="card card--front">
  <div class="card__backdrop" role="img" aria-label="Dunkelblauer Hintergrund mit leuchtendem Netzwerk aus Punkten und Linien"></div>
  <div class="brand">
    <span class="brand__dot"></span>
    <span class="brand__name">Brava-Lux.ch</span>
  </div>
</section>

<section class="card card--back">
  <div class="card__backdrop" role="img" aria-label="Dunkelblauer Hintergrund mit leuchtendem Netzwerk aus Punkten und Linien"></div>
  <div class="brand">
    <span class="brand__dot"></span>
    <span class="brand__name">Brava-Lux.ch</span>
  </div>

  <div class="contact contact--left" style="top:284px">
    <svg class="contact__icon" viewBox="0 0 22 22" fill="none" stroke="#1d2236" stroke-width="1.4"><circle cx="11" cy="11" r="10"/><circle cx="11" cy="11" r="6"/><ellipse cx="11" cy="11" rx="2.6" ry="6"/><line x1="5" y1="11" x2="17" y2="11"/></svg>
    <span>www.Brava-Lux.ch</span>
  </div>
  <div class="contact contact--left" style="top:324px">
    <svg class="contact__icon" viewBox="0 0 22 22" fill="none" stroke="#1d2236" stroke-width="1.4"><circle cx="11" cy="11" r="10"/><rect x="6" y="7.5" width="10" height="7" fill="#1d2236"/><polyline points="6,7.5 11,11.5 16,7.5" stroke="#fcc31c"/></svg>
    <span>info@brava-lux.ch</span>
  </div>

  <div class="contact contact--right" style="top:266px">
    <svg class="contact__icon" viewBox="0 0 22 22"><circle cx="11" cy="11" r="11" fill="#1d2236"/><path d="M6 9.5c0-2 2.2-3 5-3s5 1 5 3l-2 .6-.6-1.6h-4.8l-.6 1.6z M7.5 12h7l1 4h-9z" fill="#fcc31c"/></svg>
    <span>+41 ( 0 ) 79 384 6027</span>
  </div>
  <div class="contact contact--right" style="top:305px">
    <svg class="contact__icon" viewBox="0 0 22 22" fill="none" stroke="#1d2236" stroke-width="1.4"><circle cx="11" cy="11" r="10"/><path d="M11 16.5s-4-4-4-7a4 4 0 0 1 8 0c0 3-4 7-4 7z"/><circle cx="11" cy="9.5" r="1.4"/></svg>
    <span>Kellerweg 14</span>
  </div>
  <div class="contact contact--right contact--noicon" style="top:345px">
    <span>9405 Ostheim</span>
  </div>
</section>

</body>
</html>
```